Freight broker online presence/customer portal track shipping

I sleek design showing what we do, broker freight. What we specialize in, chemicals and any freight where domestic or international. We want a home page, a customer portal button on front page that lets clients check on status of their freight (integrate with our transportation management system. Contact page,
Target Market(s)
COMPANIES THAT HAVE PALLETS TO MOVE.
EXAMPLE WEBSITE FROM THE SAME INDUSTRY
https://www.mossvalecargo.com/
https://www.corventa.com/
https://www.tkwalden.com/
Number of Pages Required
3 page
Look and feel
Each slider illustrates characteristics of the customer's brand and the style your logo design should communicate.

```html
<!DOCTYPE html>
<html lang="en">
<head>
<meta charset="utf-8">
<title>Freight Broker</title>
<link rel="stylesheet" href="https://fonts.googleapis.com/css2?family=Nunito:wght@400;600;700;800&family=Nunito+Sans:wght@400;600;700&display=swap">
<style>
:root{
  --blue:#0b4a90;
  --blue-dark:#0a3b7e;
  --gold:#f2b705;
  --red:#ef4f57;
  --teal:#2db3a0;
  --teal-bar:#28a99a;
  --ink:#222;
  --muted:#777;
  --white:#fff;
}
*{margin:0;padding:0;box-sizing:border-box}
html,body{width:1200px;height:4655px;overflow:hidden}
body{position:relative;font-family:"Nunito Sans",Arial,sans-serif;color:var(--ink);background:#fff}
.abs{position:absolute}
.btn{position:absolute;display:flex;align-items:center;justify-content:center;border-radius:24px;color:#fff;font-family:"Nunito",sans-serif;font-weight:700;font-size:14px}
.btn-red{background:var(--red)}
.btn-teal{background:var(--teal)}
.photo{position:absolute}
.rule{position:absolute;height:4px;width:80px;background:var(--gold)}
.section-title{position:absolute;left:0;width:1200px;text-align:center;font-family:"Nunito",sans-serif;font-weight:700;font-size:40px;color:var(--blue);letter-spacing:.5px}

/* hero */
.hero{position:absolute;left:0;top:0;width:1200px;height:656px;background:linear-gradient(100deg,#3c3f49 0%,#6f6c74 30%,#a88580 55%,#d99a7c 75%,#e8b08a 100%)}
.brand{position:absolute;left:112px;top:32px;font-family:"Nunito",sans-serif;font-weight:700;font-size:28px;color:#fff}
.nav{position:absolute;top:47px;font-size:13px;color:#fff;font-family:"Nunito",sans-serif}
.nav.active{color:#f5a623}
.portal{position:absolute;left:952px;top:33px;width:131px;height:47px;border:1.5px solid #fff;border-radius:24px;color:#fff;font-size:13px;display:flex;align-items:center;justify-content:center;font-family:"Nunito",sans-serif}
.hero-title{position:absolute;left:683px;top:248px;font-family:"Nunito",sans-serif;font-weight:700;font-size:64px;color:#fff}
.hero-text{position:absolute;left:685px;top:328px;width:440px;font-size:14px;line-height:28px;color:#fff}
.dots{position:absolute;left:567px;top:611px;display:flex;gap:6px}
.dots span{width:12px;height:12px;border-radius:50%;background:#fff}

/* about */
.about{position:absolute;left:0;top:656px;width:600px;height:513px;background:var(--blue)}
.about h2{position:absolute;left:112px;top:118px;font-family:"Nunito",sans-serif;font-weight:700;font-size:42px;color:#fff}
.about p{position:absolute;left:112px;top:185px;width:450px;font-size:14.5px;line-height:32.5px;color:#fff}

/* cards */
.card-title{position:absolute;font-family:"Nunito",sans-serif;font-weight:600;font-size:14.5px;color:#222}
.card-text{position:absolute;width:300px;font-size:12.5px;line-height:27px;color:var(--muted)}
.spec-title{position:absolute;font-family:"Nunito",sans-serif;font-weight:700;font-size:24px;line-height:33px;color:var(--blue)}
.spec-text{position:absolute;font-size:14.5px;line-height:32.5px;color:var(--muted)}

/* tms */
.tms{position:absolute;left:0;top:2974px;width:1200px;height:514px;background:linear-gradient(180deg,#2b3446 0%,#1d2434 55%,#121621 100%)}
.tms h2{position:absolute;left:0;width:1200px;top:161px;text-align:center;font-family:"Nunito",sans-serif;font-weight:600;font-size:34px;color:#fff}
.tms p{position:absolute;left:165px;width:870px;top:210px;text-align:center;font-size:14.5px;line-height:32.5px;color:#fff}

/* news */
.news-card{position:absolute;top:3659px;width:300px;height:438px;background:#fff;box-shadow:0 2px 8px rgba(0,0,0,.15)}
.news-card .img{position:absolute;left:0;top:0;width:300px;height:257px}
.news-date{position:absolute;left:17px;top:282px;font-size:14px;color:#666;display:flex;align-items:center;gap:4px}
.news-head{position:absolute;left:0;top:308px;width:290px;font-family:"Nunito",sans-serif;font-weight:400;font-size:14.5px;line-height:25px;color:#222;border-left:3px solid var(--blue);padding-left:14px}
.news-text{position:absolute;left:17px;top:362px;width:280px;font-size:12px;line-height:25px;color:var(--muted)}

/* footer */
.footer{position:absolute;left:0;top:4201px;width:1200px;height:383px;background:linear-gradient(180deg,#0f4f97,#1a5ca2)}
.footer h3{position:absolute;font-family:"Nunito",sans-serif;font-weight:700;font-size:20px;color:#fff}
.footer .brand-f{position:absolute;left:94px;top:76px;font-family:"Nunito",sans-serif;font-weight:700;font-size:28px;color:#fff}
.footer p,.footer ul{position:absolute;font-size:13px;line-height:26px;color:#fff;list-style:none}
.social{position:absolute;top:300px;width:38px;height:38px;border:1.5px solid #fff;display:flex;align-items:center;justify-content:center}
.social i{width:10px;height:10px;border-radius:50%;background:#fff}
.copy{position:absolute;left:0;top:4584px;width:1200px;height:71px;background:var(--teal-bar);display:flex;align-items:center;justify-content:center;font-size:13px;color:#111}
</style>
</head>
<body>

<header class="hero">
  <div class="photo" role="img" aria-label="Close-up of a silver truck cab on a road at sunset" style="left:0;top:0;width:1200px;height:656px;background:linear-gradient(100deg,rgba(40,44,54,.6) 0%,rgba(0,0,0,0) 60%)"></div>
  <div class="brand">Freight Broker</div>
  <nav>
    <span class="nav active" style="left:416px">Home</span>
    <span class="nav" style="left:483px">About</span>
    <span class="nav" style="left:549px">What We Do</span>
    <span class="nav" style="left:661px">What We Specialize</span>
    <span class="nav" style="left:817px">News</span>
    <span class="nav" style="left:882px">Contact</span>
    <span class="portal">Custom Portal</span>
  </nav>
  <h1 class="hero-title">Freight Broker</h1>
  <p class="hero-text">Lorem ipsum dolor sit amet, consectetur adipiscing elit, sed do eiusmod tempor incididunt ut labore et dolore magna aliqua. Ut enim ad minim veniam</p>
  <span class="btn" style="left:685px;top:421px;width:156px;height:43px;background:var(--blue-dark)">Get Started</span>
  <div class="dots"><span></span><span></span><span></span><span></span></div>
</header>

<section class="about">
  <div class="rule" style="left:112px;top:104px"></div>
  <h2>ABOUT US</h2>
  <p>Lorem ipsum dolor sit amet, consectetur adipiscing elit, sed do eiusmod tempor incididunt ut labore et dolore magna aliqua. Ut enim ad minim veniam, quis nostrud exercitation ullamco laboris nisi ut aliquip ex ea commodo consequat. Duis aute irure dolor in reprehenderit in voluptate velit</p>
  <span class="btn btn-teal" style="left:112px;top:365px;width:155px;height:43px">Read More</span>
</section>
<div class="photo" role="img" aria-label="Stacked shipping containers under a red gantry crane at a port" style="left:600px;top:656px;width:600px;height:513px;background:linear-gradient(180deg,#9fc3e0 0%,#c0564a 35%,#3f6a98 65%,#8a7b6d 100%)"></div>

<section>
  <div class="rule" style="left:553px;top:1271px"></div>
  <h2 class="section-title" style="top:1288px">WHAT WE DO</h2>

  <div class="photo" role="img" aria-label="Freight trains in a rail yard at dusk" style="left:112px;top:1357px;width:318px;height:300px;background:linear-gradient(180deg,#6e6a8e 0%,#d99a78 40%,#6b4a40 70%,#3a2f2c 100%)"></div>
  <div class="photo" role="img" aria-label="Black semi truck driving on a tree-lined highway" style="left:443px;top:1357px;width:318px;height:300px;background:linear-gradient(180deg,#d6e3c8 0%,#7f9a55 40%,#4b5a3c 65%,#8c8f92 100%)"></div>
  <div class="photo" role="img" aria-label="Container ship at sea seen from above" style="left:772px;top:1357px;width:318px;height:300px;background:linear-gradient(135deg,#1e7fb6 0%,#2a95c8 40%,#b65a4c 60%,#1b6fa2 100%)"></div>

  <div class="card-title" style="left:112px;top:1676px">LOREM IPSUM DOLOR SIT AMET</div>
  <div class="card-title" style="left:443px;top:1676px">LOREM IPSUM DOLOR SIT AMET</div>
  <div class="card-title" style="left:772px;top:1676px">LOREM IPSUM DOLOR SIT AMET</div>
  <p class="card-text" style="left:112px;top:1706px">sed do eiusmod tempor incididunt ut labore et dolore magna aliqua. Ut enim ad minim veniam, quis nostrud exercitation ullamco</p>
  <p class="card-text" style="left:443px;top:1706px">sed do eiusmod tempor incididunt ut labore et dolore magna aliqua. Ut enim ad minim veniam, quis nostrud exercitation ullamco</p>
  <p class="card-text" style="left:772px;top:1706px">sed do eiusmod tempor incididunt ut labore et dolore magna aliqua. Ut enim ad minim veniam, quis nostrud exercitation ullamco</p>
  <span class="btn btn-red" style="left:112px;top:1802px;width:155px;height:43px">Read More</span>
  <span class="btn btn-red" style="left:443px;top:1802px;width:155px;height:43px">Read More</span>
  <span class="btn btn-red" style="left:772px;top:1802px;width:155px;height:43px">Read More</span>
</section>

<section>
  <div class="rule" style="left:553px;top:1950px"></div>
  <h2 class="section-title" style="top:1966px">WHAT WE SPECIALIZE IN</h2>

  <div class="photo" role="img" aria-label="Chemical refinery lit up at dusk under a cloudy sky" style="left:112px;top:2071px;width:448px;height:390px;border-radius:18px;box-shadow:0 4px 10px rgba(0,0,0,.2);background:linear-gradient(180deg,#5d6a7c 0%,#8a95a3 40%,#c27a3a 70%,#3b2e2a 100%)"></div>
  <h3 class="spec-title" style="left:600px;top:2124px">CHEMICALS</h3>
  <p class="spec-text" style="left:600px;top:2170px;width:485px">Lorem ipsum dolor sit amet, consectetur adipiscing elit, sed do eiusmod tempor incididunt ut labore et dolore magna aliqua. Ut enim ad minim veniam, quis nostrud exercitation ullamco laboris nisi ut aliquip ex ea commodo consequat. Duis aute irure dolor in reprehenderit in voluptate</p>
  <span class="btn btn-red" style="left:600px;top:2358px;width:155px;height:43px">Read More</span>

  <h3 class="spec-title" style="left:112px;top:2522px;width:420px">FREIGHT WHERE DOMESTIC OR INTERNATIONAL</h3>
  <p class="spec-text" style="left:112px;top:2600px;width:485px">Lorem ipsum dolor sit amet, consectetur adipiscing elit, sed do eiusmod tempor incididunt ut labore et dolore magna aliqua. Ut enim ad minim veniam, quis nostrud exercitation ullamco laboris nisi ut aliquip ex ea commodo consequat. Duis aute irure dolor in reprehenderit in voluptate</p>
  <span class="btn btn-red" style="left:112px;top:2783px;width:155px;height:43px">Read More</span>
  <div class="photo" role="img" aria-label="Cargo plane, cranes and a truck against an orange sunset" style="left:636px;top:2481px;width:448px;height:392px;border-radius:18px;box-shadow:0 4px 10px rgba(0,0,0,.2);background:linear-gradient(180deg,#7c8ea6 0%,#e7b583 40%,#e98a4a 60%,#3d4c6e 100%)"></div>
</section>

<section class="tms" role="img" aria-label="Truck on a road at night under a dark blue sky">
  <div class="abs" style="left:560px;top:130px;width:80px;height:4px;background:var(--red)"></div>
  <h2>TRANSPORTATION MANAGEMENT SYSTEM</h2>
  <p>Lorem ipsum dolor sit amet, consectetur adipiscing elit, sed do eiusmod tempor incididunt ut labore et dolore magna aliqua. Ut enim ad minim veniam, quis nostrud exercitation ullamco laboris nisi ut aliquip ex ea commodo consequat. Duis aute irure dolor in reprehenderit in voluptate</p>
  <span class="btn btn-teal" style="left:522px;top:339px;width:156px;height:43px">Contact Now</span>
</section>

<section>
  <h2 class="section-title" style="top:3584px">LATEST NEWS</h2>

  <article class="news-card" style="left:125px">
    <div class="img" role="img" aria-label="Port worker in safety gear near cranes and containers" style="background:linear-gradient(180deg,#7aa4cf 0%,#5a8a6b 45%,#c0523e 75%,#2f3a3d 100%)"></div>
    <div class="news-date"><svg width="12" height="12" viewBox="0 0 12 12"><rect x="1" y="2" width="10" height="9" fill="none" stroke="#666" stroke-width="1.4"/><rect x="1" y="2" width="10" height="3" fill="#666"/></svg>30-JUNE-2021</div>
    <h3 class="news-head">LOREM IPSUM DOLOR SIT AMET, CONSECTETUR ADIPISCING</h3>
    <p class="news-text">sed do eiusmod tempor incididunt ut labore et dolore magna aliqua. Ut enim ad minim</p>
  </article>
  <article class="news-card" style="left:455px">
    <div class="img" role="img" aria-label="Warehouse workers checking boxes on a clipboard" style="background:linear-gradient(180deg,#3f5b88 0%,#6a7390 40%,#b99a6a 70%,#7a6a55 100%)"></div>
    <div class="news-date"><svg width="12" height="12" viewBox="0 0 12 12"><rect x="1" y="2" width="10" height="9" fill="none" stroke="#666" stroke-width="1.4"/><rect x="1" y="2" width="10" height="3" fill="#666"/></svg>30-JUNE-2021</div>
    <h3 class="news-head">LOREM IPSUM DOLOR SIT AMET, CONSECTETUR ADIPISCING</h3>
    <p class="news-text">sed do eiusmod tempor incididunt ut labore et dolore magna aliqua. Ut enim ad minim</p>
  </article>
  <article class="news-card" style="left:784px">
    <div class="img" role="img" aria-label="Two workers walking through a warehouse aisle" style="background:linear-gradient(90deg,#1f2c3c 0%,#4e5a66 45%,#a07a4e 75%,#35404c 100%)"></div>
    <div class="news-date"><svg width="12" height="12" viewBox="0 0 12 12"><rect x="1" y="2" width="10" height="9" fill="none" stroke="#666" stroke-width="1.4"/><rect x="1" y="2" width="10" height="3" fill="#666"/></svg>30-JUNE-2021</div>
    <h3 class="news-head">LOREM IPSUM DOLOR SIT AMET, CONSECTETUR ADIPISCING</h3>
    <p class="news-text">sed do eiusmod tempor incididunt ut labore et dolore magna aliqua. Ut enim ad minim</p>
  </article>
</section>

<footer class="footer">
  <div class="brand-f">Freight Broker</div>
  <p style="left:94px;top:120px;width:275px;font-size:13px;line-height:25px">Lorem ipsum dolor sit amet, consectetur adipiscing elit, sed do eiusmod tempor incididunt ut labore et dolore magna aliqua. Ut enim ad minim veniam</p>
  <h3 style="left:94px;top:250px;font-size:16px">FOLLOW US</h3>
  <span class="social" style="left:96px" aria-label="Social link"><i></i></span>
  <span class="social" style="left:146px" aria-label="Social link"><i></i></span>
  <span class="social" style="left:196px" aria-label="Social link"><i></i></span>
  <span class="social" style="left:246px" aria-label="Social link"><i></i></span>
  <div class="abs" style="left:407px;top:80px;width:1px;height:235px;background:rgba(255,255,255,.7)"></div>
  <h3 style="left:451px;top:84px">LINKS</h3>
  <ul style="left:451px;top:120px"><li>Home</li><li>About</li><li>What We Do</li><li>What We Specialize</li><li>News</li><li>Contact</li></ul>
  <h3 style="left:638px;top:84px">CONTACT US</h3>
  <ul style="left:638px;top:120px;width:270px"><li>Lorem ipsum dolor sit amet, consectetur</li><li>adipiscing elit, sed do</li><li>Phone:</li><li>Phone: 555-014-2290</li><li>Fax: 555-014-7731</li></ul>
  <h3 style="left:938px;top:84px">HELP US</h3>
  <ul style="left:938px;top:120px"><li>Privacy Policy</li><li>Information</li><li>Terms &amp; Conditions</li></ul>
</footer>
<div class="copy">©2021 All Rights Reserved</div>

</body>
</html>
```